Presentation to the board mirroring the business plan and strategy

Need a power point presentation with videos, visuals to show a positive story to proceed forward with this strategy including the merger of excel sheets with P&L numbers and figures, videos and also a word document to mirror PowerPoint

Target Market(s)

Is the board of directors

Industry/Entity Type

Telecommunications - follow logo for Corvalith

Font styles to use
Serif

Colors
0054AA
0677BA
7BADD7
CADEEF
E8F1F8

Requirements
Must have
• Project must include all the budgeted numbers and graphs with targets showing growth
Nice to have
• I will attach a PowerPoint with some information and flow - need to improve this as the look is poor and clumsy. Also this video embedded into the power point from YouTube - https://www.vidmorast.net/watch?v=Kt7pLmQ2xZa
Should not have
• Should have all the numbers from excel

```html
<!DOCTYPE html>
<html lang="en">
<head>
<meta charset="utf-8">
<title>Design submission – Corvalith board presentation</title>
<link href="https://fonts.googleapis.com/css2?family=Lato:wght@400;700&family=Libre+Baskerville:wght@400;700&display=swap" rel="stylesheet">
<style>
  :root{
    --canvas:#ffffff;
    --panel:#e9e9e9;
    --panel-line:#cfcfcf;
    --column:#6b6860;
    --ink:#222222;
    --muted:#555555;
    --link:#1a82e2;
    --button-ink:#3d4a5c;
    --row:#ebebeb;
    --row-line:#cccccc;
    --mark:#e3101a;
    --navy:#0a1a3a;
    --brand:#0054AA;
    --brand-mid:#0677BA;
    --brand-soft:#7BADD7;
    --brand-pale:#CADEEF;
    --brand-mist:#E8F1F8;
  }
  *{box-sizing:border-box;margin:0;padding:0}
  html,body{width:1200px;height:225px;overflow:hidden;background:var(--canvas)}
  body{position:relative;font-family:"Lato",Arial,sans-serif;color:var(--ink)}

  .thumb-panel{position:absolute;left:8px;top:8px;width:279px;height:211px;background:var(--panel);border:1px solid var(--panel-line)}
  .page-column{position:absolute;left:86px;top:0;width:106px;height:209px;background:var(--column)}
  .page{position:absolute;left:9px;width:88px;height:62px;background:#fff;overflow:hidden}
  .page--cover{top:7px}
  .page--contents{top:74px}
  .page--summary{top:140px}
  .cover-visual{position:absolute;left:0;top:0;width:44px;height:62px;background:radial-gradient(circle at 50% 40%,#2a8fd6 0%,#0b2a5c 45%,var(--navy) 100%)}
  .cover-wave{position:absolute;right:0;bottom:0;width:44px;height:26px;background:linear-gradient(160deg,var(--brand-soft),var(--brand) 70%)}
  .cover-name{position:absolute;left:47px;top:8px;font:700 3px/1.2 "Libre Baskerville",Georgia,serif;color:var(--brand)}
  .cover-title{position:absolute;left:47px;top:14px;width:40px;font:700 2.6px/1.3 "Libre Baskerville",Georgia,serif;color:var(--navy)}
  .contents-visual{position:absolute;left:0;top:0;width:44px;height:62px;background:linear-gradient(180deg,#0f3d5c 0%,#2b9bb8 45%,#c46a2a 100%)}
  .contents-word{position:absolute;left:3px;top:30px;width:40px;text-align:center;font:400 3px/1.5 "Libre Baskerville",Georgia,serif;color:#fff}
  .line{position:absolute;height:1px;background:#b9c6d4}
  .line--head{background:var(--brand-mid);height:1.5px}
  .table-band{position:absolute;left:46px;top:44px;width:38px;height:8px;background:var(--navy)}

  .design-title{position:absolute;left:308px;top:9px;font-size:20px;font-weight:700;color:var(--ink)}
  .design-title .number{color:var(--link);font-weight:400}
  .submitted{position:absolute;right:12px;top:12px;font-size:12.5px;color:var(--muted)}

  .action{position:absolute;top:47px;height:41px;border:2px solid var(--button-ink);display:flex;align-items:center;justify-content:center;font-size:12.5px;letter-spacing:.01em;color:var(--button-ink);text-transform:uppercase;background:#fff}
  .action--source{left:308px;width:177px}
  .action--linked{left:490px;width:206px}

  .file-row{position:absolute;height:41px;background:var(--row);border:1px solid var(--row-line);display:flex;align-items:center;padding:0 12px 0 14px}
  .file-row svg{width:18px;height:20px;flex:none;margin-right:8px}
  .file-label{font-size:17px;color:var(--ink)}
  .help{display:inline-block;width:13px;height:13px;border:1.5px solid #444;border-radius:50%;font-size:9px;line-height:10px;text-align:center;margin-left:6px;vertical-align:2px;font-weight:700}
  .download{margin-left:auto;font-size:14px;color:var(--link);letter-spacing:.02em}
  .row--preview{left:308px;top:110px;width:429px}
  .row--thumbnail{left:759px;top:110px;width:429px}
  .row--zip{left:308px;top:161px;width:429px}
  .row--print{left:759px;top:161px;width:429px}

  .annotations{position:absolute;left:0;top:0;width:1200px;height:225px;pointer-events:none}
</style>
</head>
<body>

<div class="thumb-panel">
  <div class="page-column">
    <div class="page page--cover">
      <div class="cover-visual" role="img" aria-label="Cover image of a glowing globe in deep blue"></div>
      <div class="cover-wave" role="img" aria-label="Flowing blue light streaks"></div>
      <div class="cover-name">Corvalith</div>
      <div class="cover-title">CORVALITH LIMITED STRATEGY OVERVIEW PURCHASE 29% OF NORVANE</div>
    </div>
    <div class="page page--contents">
      <div class="contents-visual" role="img" aria-label="Light tunnel photograph in teal and amber"></div>
      <div class="contents-word">CONSOLIDATION, GROWTH &amp; PARTNERSHIP</div>
      <div class="line line--head" style="left:47px;top:8px;width:20px"></div>
      <div class="line" style="left:47px;top:14px;width:36px"></div>
      <div class="line" style="left:47px;top:19px;width:36px"></div>
      <div class="line" style="left:47px;top:24px;width:36px"></div>
      <div class="line" style="left:47px;top:29px;width:36px"></div>
      <div class="line" style="left:47px;top:34px;width:36px"></div>
      <div class="line" style="left:47px;top:39px;width:36px"></div>
      <div class="line" style="left:47px;top:44px;width:36px"></div>
      <div class="line" style="left:47px;top:49px;width:36px"></div>
    </div>
    <div class="page page--summary">
      <div class="line line--head" style="left:4px;top:7px;width:18px"></div>
      <div class="line line--head" style="left:46px;top:7px;width:18px"></div>
      <div class="line" style="left:4px;top:13px;width:38px"></div>
      <div class="line" style="left:4px;top:17px;width:38px"></div>
      <div class="line" style="left:4px;top:21px;width:38px"></div>
      <div class="line" style="left:4px;top:25px;width:38px"></div>
      <div class="line" style="left:4px;top:29px;width:38px"></div>
      <div class="line" style="left:4px;top:33px;width:38px"></div>
      <div class="line" style="left:4px;top:37px;width:38px"></div>
      <div class="line" style="left:4px;top:41px;width:38px"></div>
      <div class="line" style="left:4px;top:45px;width:38px"></div>
      <div class="line" style="left:4px;top:49px;width:38px"></div>
      <div class="line" style="left:46px;top:13px;width:30px"></div>
      <div class="line" style="left:46px;top:17px;width:24px"></div>
      <div class="line" style="left:46px;top:21px;width:28px"></div>
      <div class="line" style="left:46px;top:27px;width:36px"></div>
      <div class="line" style="left:46px;top:31px;width:36px"></div>
      <div class="table-band"></div>
      <div class="line" style="left:46px;top:55px;width:38px"></div>
    </div>
  </div>
</div>

<h1 class="design-title">Design #: <span class="number">37538768</span></h1>
<p class="submitted">Submitted 29-Jul-2026 | 3:54 PM</p>

<div class="action action--source">Add source files</div>
<div class="action action--linked">Submit linked design</div>

<div class="file-row row--preview">
  <svg viewBox="0 0 18 20" fill="none" stroke="#333" stroke-width="1.4"><path d="M2 1h9l5 5v13H2z"/><path d="M11 1v5h5"/></svg>
  <span class="file-label">Preview file (.jpg)<span class="help">?</span></span>
  <span class="download">DOWNLOAD</span>
</div>
<div class="file-row row--thumbnail">
  <svg viewBox="0 0 18 20" fill="none" stroke="#333" stroke-width="1.4"><rect x="1" y="3" width="16" height="15"/><path d="M3 16l4-5 3 3 2-2 4 4z" fill="#333"/><circle cx="12" cy="7" r="1.3"/></svg>
  <span class="file-label">Thumbnail file (.png)<span class="help">?</span></span>
  <span class="download">DOWNLOAD</span>
</div>
<div class="file-row row--zip">
  <svg viewBox="0 0 18 20" fill="none" stroke="#333" stroke-width="1.4"><path d="M1 4h6l2 2h8v11H1z"/></svg>
  <span class="file-label">Source file (.zip)<span class="help">?</span></span>
  <span class="download">DOWNLOAD</span>
</div>
<div class="file-row row--print">
  <svg viewBox="0 0 18 20" fill="none" stroke="#333" stroke-width="1.4"><rect x="4" y="2" width="10" height="5"/><rect x="1" y="7" width="16" height="7" rx="1"/><rect x="4" y="12" width="10" height="6"/></svg>
  <span class="file-label">Print file (not yet uploaded)</span>
</div>

<svg class="annotations" viewBox="0 0 1200 225" fill="none" stroke="var(--mark)" stroke-width="2.4" stroke-linecap="round">
  <path d="M508 21 C450 8 380 4 330 10 C300 14 288 30 300 40 C322 52 450 55 530 45 C548 40 540 20 525 0"/>
  <path d="M738 171 C600 164 400 154 320 168 C270 178 275 198 330 203 C450 210 650 208 745 196 C764 190 756 174 742 157"/>
</svg>

</body>
</html>
```